Stationary for Tovin Consulting

Hi

I am after stationary designs for my company - Tovin Consulting. I have a logo - recently designed by ArtHarbor. Tovin ( nivot spelt backwards ) is a sales consultancy - including sales training, sales coaching and business management.

I have attached some of the artwork I already have, as well as a few ideas
1. Use supplied logo's
2. back of business card to use the logo with the dark background and white text
3. details to be included on card are
Logo
Delia Marquand
p: +61409827316
e: delia@tovinconsulting.com.au
w: www.tovinconsulting.com.au
PO Box 412, Kelby Heights, Victoria, 3187

4. I am after designs for business cards, A4 letterhead and A5 letterhead

Thanks in Advance

Delia

Industry/Entity Type

It Company

```html
<!DOCTYPE html>
<html lang="en">
<head>
<meta charset="utf-8">
<title>Tovin Consulting — Business Card Back</title>
<link rel="stylesheet" href="https://fonts.googleapis.com/css2?family=Exo+2:wght@600&family=Open+Sans:wght@400&display=swap">
<style>
  :root {
    --card-deep: #1b3444;
    --card-mid: #22404f;
    --card-glow: #26475a;
    --texture-tone: #27495a;
    --ink-white: #ffffff;
  }
  * { margin: 0; padding: 0; box-sizing: border-box; }
  html, body {
    width: 1200px;
    height: 686px;
    overflow: hidden;
    background: var(--card-deep);
  }
  .card-back {
    position: relative;
    width: 1200px;
    height: 686px;
    overflow: hidden;
    background: radial-gradient(ellipse 60% 65% at 52% 45%, var(--card-glow) 0%, var(--card-mid) 50%, var(--card-deep) 100%);
  }
  .texture-band {
    position: absolute;
    inset: 0;
    width: 1200px;
    height: 686px;
  }
  .brand-name {
    position: absolute;
    left: 0;
    width: 1200px;
    text-align: center;
    font-family: "Exo 2", sans-serif;
    font-weight: 600;
    color: var(--ink-white);
  }
  .brand-name-primary {
    top: 228px;
    font-size: 150px;
    line-height: 1;
    letter-spacing: 2px;
  }
  .brand-name-secondary {
    top: 402px;
    font-size: 38px;
    line-height: 1;
    letter-spacing: 31px;
    padding-left: 31px;
  }
  .web-address {
    position: absolute;
    left: 0;
    top: 520px;
    width: 1200px;
    text-align: center;
    font-family: "Open Sans", sans-serif;
    font-weight: 400;
    font-size: 24px;
    letter-spacing: 0.6px;
    color: var(--ink-white);
  }
</style>
</head>
<body>
  <main class="card-back">
    <svg class="texture-band" viewBox="0 0 1200 686" aria-hidden="false">
      <defs>
        <linearGradient id="textureFade" x1="0" y1="0" x2="1" y2="1">
          <stop offset="0" stop-color="#2a4d5f"/>
          <stop offset="1" stop-color="#21404f"/>
        </linearGradient>
      </defs>
      <polygon role="img" aria-label="Fine diagonal pinstripe texture across the lower-left half of the card"
               points="0,12 1145,686 0,686" fill="url(#textureFade)" opacity="0.85"/>
    </svg>

    <div class="brand-name brand-name-primary">Tovin</div>
    <div class="brand-name brand-name-secondary">CONSULTING</div>

    <p class="web-address">www.tovinconsulting.com.au</p>
  </main>
</body>
</html>
```